IT Network Consultancy - Business Card

kelbrin systems is a IT network consultancy based in London. We're looking for a smart, modern and professional business card design. Our website is here: www.kelbrinsystems.co.uk

Key things that should be included on the card (with examples):

Company Logo
Name
Position / Job Title: Network Consultant
Mobile Phone Number: +44 (0) 7700 900418
Land Line: +44 (0) 1632 960735
Email Address: name@kelbrinsystems.co.uk
Web Site URL: www.kelbrinsystems.co.uk

Target Market(s)

Large enterprise / global companies / corporates

Industry/Entity Type

Business

Requirements
Must have
• Incorporate our logo - which is attached to the project. They are in AI format (can be opened in Inkscape).

The design should be double sided and fit on a UK standard 85mm × 55mm card and be in a format that retains the quality when printed.
Nice to have
• The project does not have to conform to the colour of our website but this should give you inspiration of the style we like.
Should not have
• Bright colours. Pictures are not necessary.

```html
<!DOCTYPE html>
<html lang="en">
<head>
<meta charset="utf-8">
<title>kelbrin systems – Business Card</title>
<link rel="stylesheet" href="https://fonts.googleapis.com/css2?family=Open+Sans:wght@300;400;700&display=swap">
<style>
  :root {
    --page: #ffffff;
    --card: #ffffff;
    --card-edge: #e4e4e4;
    --card-shadow: rgba(0, 0, 0, 0.18);
    --ink: #231f20;
    --muted: #7d7f82;
    --detail: #5a5c5f;
    --brand: #8a8c8f;
    --faint: #eeeeee;
    --pattern-light: #fbfbfb;
    --pattern-mid: #f0f0f0;
    --pattern-dark: #e6e6e6;
  }
  * { margin: 0; padding: 0; box-sizing: border-box; }
  html, body {
    width: 1200px; height: 900px; overflow: hidden;
    background: var(--page);
    font-family: "Open Sans", Arial, sans-serif;
  }
  .stage { position: relative; width: 1200px; height: 900px; }

  .card {
    position: absolute;
    width: 590px; height: 382px;
    background: var(--card);
    border: 1px solid var(--card-edge);
    box-shadow: 4px 6px 10px var(--card-shadow);
    overflow: hidden;
  }
  .card--back { left: 520px; top: 393px; z-index: 1; }
  .card--front { left: 77px; top: 112px; z-index: 2; }

  .wordmark {
    position: absolute;
    color: var(--brand);
    font-weight: 300;
    text-transform: uppercase;
    white-space: nowrap;
  }

  /* Front */
  .card--front .wordmark {
    left: 190px; top: 44px;
    font-size: 29px; letter-spacing: 1.5px;
  }
  .front__accent {
    position: absolute;
    left: -40px; top: 180px;
    width: 250px; height: 250px;
    border-radius: 50%;
    background: var(--faint);
  }
  .holder { position: absolute; left: 268px; top: 150px; }
  .holder__name { font-size: 17px; font-weight: 700; color: var(--ink); line-height: 24px; }
  .holder__role { font-size: 14px; font-weight: 400; color: var(--muted); line-height: 20px; }

  .contact {
    position: absolute; left: 268px; top: 266px;
    display: grid; grid-template-columns: 90px auto;
    font-size: 14.5px; line-height: 19.5px;
  }
  .contact dt { font-weight: 700; color: var(--ink); }
  .contact dd { font-weight: 400; color: var(--detail); }

  /* Back */
  .card__pattern {
    position: absolute; inset: 0;
    background: radial-gradient(ellipse at center, var(--pattern-light) 0%, var(--pattern-mid) 55%, var(--pattern-dark) 100%);
  }
  .back__mark {
    position: absolute;
    left: 50%; top: 132px;
    width: 64px; height: 64px;
    margin-left: -32px;
    border-radius: 50%;
    background: var(--brand);
  }
  .card--back .wordmark {
    left: 0; right: 0; top: 214px;
    text-align: center;
    font-size: 24px; letter-spacing: 1.5px;
  }
</style>
</head>
<body>
<main class="stage">
  <section class="card card--back" aria-label="Business card, back">
    <div class="card__pattern" role="img" aria-label="Repeating outline pattern of the brand symbol in light grey"></div>
    <span class="back__mark" aria-hidden="true"></span>
    <p class="wordmark">kelbrin systems</p>
  </section>

  <section class="card card--front" aria-label="Business card, front">
    <span class="front__accent" aria-hidden="true"></span>
    <p class="wordmark">kelbrin systems</p>
    <div class="holder">
      <p class="holder__name">Daniel Marsh</p>
      <p class="holder__role">Network Consultant</p>
    </div>
    <dl class="contact">
      <dt>Mobile</dt><dd>+44 (0) 7700 900418</dd>
      <dt>Land Line</dt><dd>+44 (0) 1632 960735</dd>
      <dt>Email</dt><dd>name@kelbrinsystems.co.uk</dd>
      <dt>Web</dt><dd>www.kelbrinsystems.co.uk</dd>
    </dl>
  </section>
</main>
</body>
</html>
```